Suchen ansprechendes & seriöses Urkunden/Zertifikat Design für Webseite & Druck
Zielgruppe
Auf unserer Webseite http://rege-im-alter-netz.de können sich Unternehmen, Institutionen und Vereine ihre Seniorenfreundlichkeit durch ein Zertifikat bestätigen und zertifizieren lassen.
Unsere Kundengruppen: Hotel – Gastronomie – Wellness – Reisen und Touristik – Touristikregionen – Seniorenshop – Onlineshop – Unternehmen als Dienstleister – Medizin und Health-Service – Apotheke – Altenheim – Pflegeheim – Seniorenheim – Vereine – Seniorenservice – Zahnärzte – Fitnessstudio – Sportstudio – Physiotherapie – Sportverein – Golfclub – und viele weitere seniorenfreundliche Institutionen.
Aufgabenstellung
Auftrag- Ausschreibung:
- Erstellung eines Design:
- Urkunde für Webseite rege-im-alter-netz.de - Das Zertifikat "Rege im Alter“
Funktion:
Kunde erkennt das Zertifikat - Logo auf einer Webseite und Klickt auf dieses.
Er wird weitergeleitet auf eine Unterseite, worin die Richtlinien und die Urkunde sichtbar wird.
Zielgruppe:
- Unternehmen, welche das Zertifikat auf Ihre Webseite setzen. Die Urkunde gibt Auskunft, dass der Dienstleister einen besonderen Service für Senioren ausübt. Die Urkunde ist sichtbar auf der Webseite, indem das Logo angeklickt wird. Die Urkunde gibt es ebenfalls als Download, damit der Kunde diese in seinen Geschäftsräumen aufhängen kann oder diese in seinen Werbeunterlagen präsentieren kann.
- Verbraucher sollen beeindruckt sein, von der Urkunde, welches Vertrauen ausstrahlt, aber auch Seriosität
Folgende Ausstrahlung soll die Urkunde haben:
- Soll Mitbewerber des Zertifikatsinhaber beeindrucken und das Verlangen aufzeigen, sich ebenfalls zertifizieren zu lassen ( ca: 70% der Kunden sind Mitbewerber … ). Nach dem Motto "Das Logo ist super und edel, das muss ich auch haben!"
- Der Kunde als Verbraucher soll Vertrauen gewinnen, die Daten sollen gut sichtbar sein, aber nicht verkitscht wie eine Urkunde bei einer Kaffeefahrt. Der Verbraucher geht auf das Zertifikat und kommt zur Urkunde, deshalb soll die Farbe, und Darstellung, Seriosität des Unternehmens ausstrahlen.
Sonstiges
- Die Urkunde soll dem neuen Design unserer Seite (zu sehen unter: http://guetesiegel-welt.de) angepasst sein.
- Vor Auftragsendvergabe erhalten Sie noch ein telefonisches Briefing über unsere Erfahrungswerte
Link zur bestehenden alten Webseite (Altes Design): http://rege-im-alter-netz.de
Info Verbraucher: http://www.rege-im-alter-netz.de/verbraucher/
Info zum Zertifikat: http://www.rege-im-alter-ne..

```html
<!DOCTYPE html>
<html lang="de">
<head>
<meta charset="utf-8">
<title>Zertifikat – Rege im Alter</title>
<link href="https://fonts.googleapis.com/css2?family=Bebas+Neue&family=Raleway:wght@300;400;700&display=swap" rel="stylesheet">
<style>
  :root {
    --navy: #3b2f8f;
    --red: #b3262a;
    --ink: #1c1c1c;
    --frame: #d9d9d9;
    --paper-top: #ffffff;
    --paper-bottom: #ececec;
    --seal-grey: #c8c8c8;
    --sign-tone: #e2e2e2;
  }
  html, body {
    margin: 0;
    padding: 0;
    overflow: hidden;
    background: #ffffff;
  }
  .certificate {
    position: relative;
    width: 850px;
    height: 1200px;
    overflow: hidden;
    background: radial-gradient(ellipse at 50% 45%, var(--paper-top) 0%, #f6f6f6 55%, var(--paper-bottom) 100%);
    font-family: "Raleway", Arial, sans-serif;
    color: var(--ink);
  }
  .certificate__frame {
    position: absolute;
    left: 57px;
    top: 45px;
    width: 731px;
    height: 1110px;
    border: 4px solid var(--frame);
    box-sizing: border-box;
    background: rgba(255,255,255,0.55);
  }
  .band {
    position: absolute;
    background: var(--navy);
  }
  .band--thick-left  { left: 0; top: 97px; width: 165px; height: 106px; }
  .band--thick-right { right: 0; top: 97px; width: 168px; height: 106px; }
  .band--thin-left   { left: 0; top: 214px; width: 165px; height: 29px; }
  .band--thin-right  { right: 0; top: 214px; width: 168px; height: 29px; }

  .certificate__title {
    position: absolute;
    left: 0;
    right: 0;
    top: 84px;
    margin: 0;
    text-align: center;
    font-family: "Bebas Neue", "Oswald", sans-serif;
    font-weight: 400;
    font-size: 136px;
    line-height: 1;
    letter-spacing: 2px;
    color: var(--red);
  }
  .certificate__subtitle {
    position: absolute;
    left: 0;
    right: 0;
    top: 206px;
    margin: 0;
    text-align: center;
    font-weight: 300;
    font-size: 40px;
    line-height: 1;
    letter-spacing: 1px;
    text-transform: uppercase;
  }

  .detail {
    position: absolute;
    left: 0;
    width: 850px;
    display: flex;
    font-size: 27px;
    line-height: 31px;
  }
  .detail__label {
    width: 327px;
    text-align: right;
    font-weight: 700;
    flex: none;
  }
  .detail__value {
    padding-left: 12px;
    font-weight: 300;
  }
  .detail--id        { top: 310px; }
  .detail--provider  { top: 370px; }
  .detail--status    { top: 466px; }
  .detail--company   { top: 530px; }
  .detail--rep       { top: 724px; }
  .detail--first     { top: 857px; }
  .detail--valid     { top: 914px; }
  .detail--confirmed { top: 1066px; }

  .seal {
    position: absolute;
    left: 522px;
    top: 790px;
    width: 230px;
    display: flex;
    flex-direction: column;
    align-items: center;
    gap: 14px;
  }
  .seal__disc {
    width: 150px;
    height: 150px;
    border-radius: 50%;
    background: var(--seal-grey);
  }
  .seal__name {
    font-weight: 700;
    font-size: 26px;
    color: var(--red);
  }

  .signature {
    position: absolute;
    top: 990px;
    height: 66px;
    border-radius: 33px;
    background: linear-gradient(90deg, rgba(226,226,226,0), var(--sign-tone) 30%, var(--sign-tone) 70%, rgba(226,226,226,0));
  }
  .signature--first  { left: 330px; width: 190px; }
  .signature--second { left: 545px; width: 220px; }

  .signer {
    position: absolute;
    top: 1072px;
    font-size: 21px;
    font-weight: 300;
    text-align: center;
  }
  .signer--first  { left: 330px; width: 150px; }
  .signer--second { left: 545px; width: 150px; }
</style>
</head>
<body>
<main class="certificate">
  <div class="certificate__frame"></div>
  <div class="band band--thick-left"></div>
  <div class="band band--thick-right"></div>
  <div class="band band--thin-left"></div>
  <div class="band band--thin-right"></div>

  <h1 class="certificate__title">Zertifikat</h1>
  <p class="certificate__subtitle">Rege im Alter</p>

  <div class="detail detail--id">
    <span class="detail__label">Zertifikat ID:</span>
    <span class="detail__value">7250441e9e</span>
  </div>
  <div class="detail detail--provider">
    <span class="detail__label">Anbieter:</span>
    <span class="detail__value">Rege im Alter<br>Ihr Zertifizierungsdienst</span>
  </div>
  <div class="detail detail--status">
    <span class="detail__label">Status:</span>
    <span class="detail__value">aktiv</span>
  </div>
  <div class="detail detail--company">
    <span class="detail__label">Unternehmen:</span>
    <span class="detail__value">Senioren Service Lindgart<br>Ahorn Str. 7<br>12345 Stadt<br>Deutschland<br>info@lindgart.org</span>
  </div>
  <div class="detail detail--rep">
    <span class="detail__label">Vertretungs-<br>berechtigter:</span>
    <span class="detail__value">Frau Helga Lindgart</span>
  </div>
  <div class="detail detail--first">
    <span class="detail__label">Erstprüfung am:</span>
    <span class="detail__value">07.04.2017</span>
  </div>
  <div class="detail detail--valid">
    <span class="detail__label">gültig bis:</span>
    <span class="detail__value">07.04.2019</span>
  </div>

  <div class="seal">
    <div class="seal__disc"></div>
    <span class="seal__name">Rege im Alter</span>
  </div>

  <div class="signature signature--first" role="img" aria-label="Handschriftliche Unterschrift von H. Brenner"></div>
  <div class="signature signature--second" role="img" aria-label="Handschriftliche Unterschrift von C. Walden"></div>

  <div class="detail detail--confirmed">
    <span class="detail__label">Bestätigt von:</span>
  </div>
  <span class="signer signer--first">H. Brenner</span>
  <span class="signer signer--second">C. Walden</span>
</main>
</body>
</html>
```